KT Crewing business card

Require business card which includes:
Company name: KT CREWING PTY LTD
Email: Mick@ktcrewing.com.au
Phone: 0431 256 049
ACN: 718 235 946

slogan: Onsite Auto Electrician Labour hire

Details and logo on top side
Logo only on bottom side

colour codes : #F15A29 , #939598

Target Market(s)

Western Australia mining sector

Industry/Entity Type

Mining

Contact Information for Business Card

Require business card which includes: Company name: KT CREWING PTY LTD Email: Mick@ktcrewing.com.au Phone: 0431 256 049 ACN: 718 235 946 slogan: Onsite Auto Electrician Labour hire Details and logo on top side Logo only on bottom side colour codes : #F15A29 , #939598

Colors
EE7325
F08F49
F5BC92
FAE3D3
FDF4ED

Requirements
Must have
• double sided

```html
<!DOCTYPE html>
<html lang="en">
<head>
<meta charset="utf-8">
<title>KT Crewing business card</title>
<link href="https://fonts.googleapis.com/css2?family=Raleway:wght@500;700;800&display=swap" rel="stylesheet">
<style>
  :root {
    --brand-orange: #F15A29;
    --brand-grey: #939598;
    --card-white: #FFFFFF;
    --backdrop: #E6E6E7;
    --ink-light: #FFFFFF;
  }
  * { box-sizing: border-box; margin: 0; padding: 0; }
  html, body {
    width: 1200px;
    height: 900px;
    overflow: hidden;
    background: var(--backdrop);
    font-family: "Raleway", Arial, sans-serif;
  }
  .sheet {
    width: 1200px;
    height: 900px;
    display: flex;
    flex-direction: column;
    align-items: center;
    justify-content: center;
    gap: 36px;
  }
  .card {
    position: relative;
    width: 700px;
    height: 400px;
    overflow: hidden;
    box-shadow: 0 6px 18px rgba(0,0,0,0.18);
  }
  .card--front {
    background: var(--brand-orange);
    display: flex;
    align-items: center;
    justify-content: center;
  }
  .wordmark {
    display: flex;
    align-items: center;
    gap: 18px;
    font-weight: 800;
    letter-spacing: 1px;
    line-height: 1;
  }
  .wordmark__mark {
    width: 34px;
    height: 34px;
  }
  .card--front .wordmark { font-size: 72px; color: var(--ink-light); }
  .card--front .wordmark__mark { background: var(--ink-light); }

  .card--back { background: var(--brand-orange); }
  .card__swoosh {
    position: absolute;
    inset: 0;
    width: 100%;
    height: 100%;
  }
  .swoosh__band { fill: var(--brand-grey); }
  .swoosh__panel { fill: var(--card-white); }

  .card--back .wordmark {
    position: absolute;
    top: 118px;
    right: 48px;
    font-size: 46px;
    color: var(--brand-orange);
  }
  .card--back .wordmark__mark {
    width: 24px;
    height: 24px;
    background: var(--brand-grey);
  }

  .company {
    position: absolute;
    left: 40px;
    top: 46px;
    color: var(--ink-light);
  }
  .company__name {
    font-size: 19px;
    font-weight: 800;
    letter-spacing: 0.5px;
  }
  .company__acn {
    margin-top: 6px;
    font-size: 17px;
    font-weight: 500;
  }

  .contact {
    position: absolute;
    left: 40px;
    bottom: 34px;
    color: var(--ink-light);
    list-style: none;
    font-size: 17px;
    font-weight: 500;
    line-height: 1.55;
  }
  .contact__item {
    display: flex;
    align-items: center;
    gap: 9px;
  }
  .contact__icon {
    width: 17px;
    height: 17px;
    fill: var(--ink-light);
    flex: none;
  }
</style>
</head>
<body>
<main class="sheet">

  <section class="card card--front" aria-label="Card front">
    <div class="wordmark">
      <span class="wordmark__mark"></span>
      <span class="wordmark__name">KT Crewing</span>
    </div>
  </section>

  <section class="card card--back" aria-label="Card back">
    <svg class="card__swoosh" viewBox="0 0 700 400" preserveAspectRatio="none" aria-hidden="true">
      <path class="swoosh__band" d="M 222 0 Q 318 322 700 338 L 700 0 Z"/>
      <path class="swoosh__panel" d="M 262 0 Q 372 292 700 330 L 700 0 Z"/>
    </svg>

    <div class="wordmark">
      <span class="wordmark__name">KT Crewing</span>
      <span class="wordmark__mark"></span>
    </div>

    <div class="company">
      <p class="company__name">KT CREWING PTY LTD</p>
      <p class="company__acn">ACN: 718 235 946</p>
    </div>

    <ul class="contact">
      <li class="contact__item">
        <svg class="contact__icon" viewBox="0 0 24 24" aria-hidden="true">
          <path d="M6.6 10.8a15.1 15.1 0 0 0 6.6 6.6l2.2-2.2a1 1 0 0 1 1-.25 11.4 11.4 0 0 0 3.6.57 1 1 0 0 1 1 1V20a1 1 0 0 1-1 1A17 17 0 0 1 3 4a1 1 0 0 1 1-1h3.5a1 1 0 0 1 1 1c0 1.25.2 2.45.57 3.57a1 1 0 0 1-.25 1z"/>
        </svg>
        <span>0431 256 049</span>
      </li>
      <li class="contact__item">
        <svg class="contact__icon" viewBox="0 0 24 24" aria-hidden="true">
          <path d="M2 5h20v14H2z M3.5 6.5 12 13l8.5-6.5" stroke="#F15A29" stroke-width="1.4" stroke-linejoin="round"/>
        </svg>
        <span>Mick@ktcrewing.com.au</span>
      </li>
      <li class="contact__item">
        <span>Onsite Auto Electrician Labour hire</span>
      </li>
    </ul>
  </section>

</main>
</body>
</html>
```